Letterhead for a German Distribution/Manufacturing Company

We need a professional Letterhead in a unique Design.
not to playful.
The Letterhead has to show show that we are a international company with headquater in Germany.
all details like adress, Vat Tax Number, Bank Accout, Eori, email, Company number has to be on the Letterhead.
for example use: VAT TAX DE5704168 Bank Account: Norrfeld Bank IBAN DE421705238ß310482 Swift: KOLV3154802 EORI 3041296587 Company Number: HRB 61508 Adress: VOLTRINA UG Amsel Strasse 7 Postal Code 04683 City Burgstädt Country: Germany Email: info@voltrina-example.com
the design can be colored but doesnt have to be
Industry/Entity Type
Manufacturing and international distribution
Requirements
Must have
- show that we are a international company with headquater in Germany. our company infos and logo

```html
<!DOCTYPE html>
<html lang="en">
<head>
<meta charset="utf-8">
<title>VOLTRINA UG Letterhead</title>
<link rel="stylesheet" href="https://fonts.googleapis.com/css2?family=Tinos&display=swap">
<style>
  :root {
    --backdrop: #f2f2f2;
    --paper: #ffffff;
    --ink: #333333;
    --ink-dark: #111111;
    --brand-dark: #515151;
    --brand-light: #a3a3a3;
  }
  * { margin: 0; padding: 0; box-sizing: border-box; }
  html, body {
    width: 1200px; height: 1200px; overflow: hidden;
    background: var(--backdrop);
    font-family: "Tinos", "Times New Roman", serif;
    color: var(--ink);
  }
  .letterhead {
    position: absolute; left: 136px; top: 0;
    width: 1184px; height: 1532px;
    background: var(--paper);
    transform: scale(0.7833); transform-origin: top left;
    overflow: hidden;
  }
  .brand-block {
    position: absolute; left: 83px; top: 0; width: 244px; height: 220px;
    background: var(--brand-dark);
    display: flex; align-items: center; justify-content: center; gap: 10px;
  }
  .brand-mark { width: 22px; height: 22px; border-radius: 50%; background: var(--paper); }
  .brand-name { color: var(--paper); font-size: 26px; letter-spacing: 1px; }
  .header-rule {
    position: absolute; left: 327px; top: 166px; width: 857px; height: 17px;
    background: var(--brand-light);
  }
  .recipient { position: absolute; left: 84px; top: 252px; color: var(--ink-dark); }
  .recipient .label { font-size: 21px; }
  .recipient .role { font-size: 15px; margin-top: 4px; }
  .date { position: absolute; right: 98px; top: 313px; font-size: 25px; color: var(--ink-dark); }
  .account-details { position: absolute; left: 84px; top: 366px; font-size: 20px; line-height: 25px; }
  .body-copy {
    position: absolute; left: 84px; top: 476px; width: 1006px;
    font-size: 29px; line-height: 32.7px; letter-spacing: -0.25px; text-align: justify;
  }
  .body-copy p + p { margin-top: 32.7px; }
  .sign-off { position: absolute; left: 84px; top: 1066px; font-size: 30px; }
  .signature {
    position: absolute; left: 88px; top: 1112px; width: 188px; height: 32px;
    background: linear-gradient(90deg, #222 0%, #666 100%); opacity: .15; border-radius: 16px;
  }
  .company-address { position: absolute; left: 670px; top: 1114px; font-style: normal; }
  .company-address .country { font-size: 32px; line-height: 36px; }
  .company-address .lines { font-size: 25px; line-height: 31px; }
  .footer-band {
    position: absolute; left: 0; top: 1300px; width: 1184px; height: 232px;
    background: linear-gradient(180deg, rgba(163,163,163,0) 0%, var(--brand-light) 45%, var(--brand-dark) 100%);
  }
</style>
</head>
<body>
  <main class="letterhead">
    <header class="brand-block">
      <span class="brand-mark"></span>
      <span class="brand-name">VOLTRINA</span>
    </header>
    <div class="header-rule"></div>

    <div class="recipient">
      <div class="label">TO</div>
      <div class="role">President / CEO</div>
    </div>
    <div class="date">1, april, 2023</div>

    <div class="account-details">
      <div>VAT TAX DE5704168</div>
      <div>Norrfeld Bank IBAN DE421705238ß310482</div>
    </div>

    <section class="body-copy">
      <p>Lorem Ipsum is simply dummy text of the printing and typesetting industry. Lorem Ipsum has been the industry's standard dummy text ever since the 1500s, when an unknown printer took a galley of type and scrambled it to make a type specimen book. It has survived not only five centuries, but also the leap into electronic typesetting, remaining essentially unchanged. It was popularised in the 1960s with the release of Lettrafix sheets containing Lorem Ipsum passages, and more recently with desktop publishing software like Quillo PageSetter including versions of Lorem Ipsum.</p>
      <p>It is a long established fact that a reader will be distracted by the readable content of a page when looking at its layout. The point of using Lorem Ipsum is that it has a more-or-less normal distribution of letters, as opposed to using 'Content here, content here', making it look like readable English. Many desktop publishing packages and web page editors now use Lorem Ipsum as their default model text, and a search for 'lorem ipsum' will uncover many web sites still in their infancy. Various versions have evolved over the years, sometimes by accident, sometimes on purpose (injected humour and the like).</p>
    </section>

    <div class="sign-off">Director</div>
    <div class="signature" role="img" aria-label="Director's handwritten signature"></div>

    <address class="company-address">
      <div class="country">GERMANY</div>
      <div class="lines">
        <div>VOLTRINA UG Amsel Strasse 7 Postal</div>
        <div>KOLV3154802 EORI 3041296587</div>
        <div>HRB 61508</div>
        <div>info@voltrina-example.com</div>
      </div>
    </address>

    <div class="footer-band" role="img" aria-label="Decorative grey wave ornament along the foot of the page"></div>
  </main>
</body>
</html>
```